Consulting firm needs a professional letterhead design

We need a professional letterhead design which is simple but unique. It should carry attributes of the latest designs in the market suitable for professional environmental consultancies.

- The logo is attached for you to USE.
- Our preferred color scheme is that shown in the logo.
- Letterhead text color is your choice to make.
- Logo to the left and text to the right plus slogan/tagline is desirable for this letterhead.

Use any address etc. of your choice in the letterhead.

Target Market(s)

Consulting firms and government agencies

Industry/Entity Type

Environmental Consultant

Colors
acd037
fece3e
85cae6
3277b5

Requirements
Must have
• Logo supplied and color scheme must be used.
Nice to have
• Nexa font is used in the Logo, so it would ne nice to have nexa font in the letterhead too.

```html
<!DOCTYPE html>
<html lang="en">
<head>
<meta charset="utf-8">
<title>Verdantis Letterhead</title>
<link href="https://fonts.googleapis.com/css2?family=Arimo&family=Open+Sans:wght@400&family=Montserrat:wght@600&display=swap" rel="stylesheet">
<style>
  :root {
    --brand-teal: #0c86a6;
    --brand-orange: #f9a81c;
    --brand-blue: #3277b5;
    --body-text: #555a5e;
    --paper: #ffffff;
  }
  html, body { margin: 0; padding: 0; overflow: hidden; background: var(--paper); }
  .letterhead {
    position: relative;
    width: 855px;
    height: 1200px;
    overflow: hidden;
    background: var(--paper);
    font-family: "Arimo", Arial, sans-serif;
    color: var(--body-text);
    font-size: 12.4px;
    line-height: 13.3px;
  }
  .header-band { position: absolute; left: 0; top: 0; width: 855px; height: 37px; }
  .brand {
    position: absolute; left: 138px; top: 68px;
    display: flex; align-items: center; gap: 8px;
  }
  .brand-dot { width: 26px; height: 26px; border-radius: 50%; background: var(--brand-teal); }
  .brand-name {
    font-family: "Montserrat", sans-serif; font-weight: 600;
    font-size: 17px; letter-spacing: 1px; color: var(--brand-blue);
  }
  .block { position: absolute; left: 137px; width: 575px; margin: 0; }
  .letter-date { top: 197px; }
  .recipient { top: 224px; }
  .salutation { top: 291px; }
  .para-1 { top: 318px; }
  .para-2 { top: 358px; }
  .para-3 { top: 398px; }
  .para-4 { top: 479px; }
  .closing { top: 560px; }
  .signature { top: 614px; }
  .footer-band { position: absolute; left: 0; top: 1092px; width: 855px; height: 108px; }
  .slogan {
    position: absolute; left: 138px; top: 1094px; width: 150px; height: 28px;
    display: flex; align-items: center; justify-content: center;
    font-family: "Open Sans", sans-serif; font-size: 11px; color: #fff;
  }
  .contact-row {
    position: absolute; top: 1160px; left: 0; width: 855px; height: 20px;
    font-family: "Open Sans", sans-serif; font-size: 10.6px; color: #fff;
  }
  .contact-item { position: absolute; top: 0; display: flex; align-items: center; gap: 12px; white-space: nowrap; }
  .contact-item svg { flex: none; }
  .contact-address { left: 155px; }
  .contact-email { left: 414px; }
  .contact-web { left: 570px; }
</style>
</head>
<body>
<div class="letterhead">
  <svg class="header-band" viewBox="0 0 855 37" aria-hidden="true">
    <rect x="0" y="0" width="855" height="24" fill="var(--brand-teal)"/>
    <path d="M140 23 L285 23 L279 33 Q277 36 273 36 L151 36 Q147 36 145 33 Z" fill="var(--brand-teal)"/>
  </svg>

  <div class="brand">
    <span class="brand-dot"></span>
    <span class="brand-name">VERDANTIS</span>
  </div>

  <p class="block letter-date">August 28, 2011</p>
  <p class="block recipient">First Last Name<br>Street Address<br>City, State 00000</p>
  <p class="block salutation">Dear :</p>
  <p class="block para-1">Lorem ipsum dolor sit amet, consectetur adipiscing elit. Aenean ut ipsum eget massa hendrerit vestibulum vel in velit. Donec pretium neque velit.</p>
  <p class="block para-2">Aliquam porta lectus nec mauris ornare venenatis. Vivamus non est turpis, et cursus sem. Mauris vehicula erat in diam auctor at bibendum nisl lacinia.</p>
  <p class="block para-3">Morbi imperdiet neque vehicula nunc convallis gravida. Vestibulum iaculis pretium placerat. Integer consequat, est sit amet facilisis eleifend, nibh nibh varius orci, eget dapibus arcu dui non purus. Pellentesque in magna mauris. Duis enim sapien, dictum vitae condimentum a, pulvinar vel lacus. Mauris et molestie nibh. Vestibulum vitae nulla at metus elementum porta sit amet interdum elit. Nulla sollicitudin neque eu nulla volutpat congue.</p>
  <p class="block para-4">Etiam pellentesque, velit id dapibus fermentum, turpis sapien ornare dui, ac tincidunt ligula odio congue purus. Nunc sed ante dui, in porta lectus. Cras nec sem lorem. In hac habitasse platea dictumst. Maecenas id diam quis dui porta tristique. Sed id egestas felis. Donec ullamcorper mattis posuere. Phasellus fermentum eleifend tortor vel dapibus. Vestibulum ante ipsum.</p>
  <p class="block closing">Sincerely,</p>
  <p class="block signature">Daniel Harlow<br>HarlowAdvisory.com<br>P.O. Box 000000<br>Ridgeway, CO 80512<br>P: (970) 555-0187</p>

  <svg class="footer-band" viewBox="0 1092 855 108" aria-hidden="true">
    <rect x="0" y="1101" width="855" height="99" fill="var(--brand-teal)"/>
    <path d="M146 1094 L278 1094 Q282 1094 284 1097 L290 1108 L282 1120 Q280 1122 276 1122 L146 1122 Q142 1122 140 1119 L134 1108 L140 1097 Q142 1094 146 1094 Z" fill="var(--brand-orange)"/>
  </svg>
  <div class="slogan">your slogan text</div>

  <div class="contact-row">
    <div class="contact-item contact-address">
      <svg width="8" height="12" viewBox="0 0 8 12" aria-hidden="true"><path d="M4 0 A4 4 0 0 1 8 4 C8 7 4 12 4 12 C4 12 0 7 0 4 A4 4 0 0 1 4 0 Z" fill="#fff"/><circle cx="4" cy="4" r="1.5" fill="var(--brand-teal)"/></svg>
      <span>1204/56 Harbour Lane, Brisbane QLD 4000</span>
    </div>
    <div class="contact-item contact-email">
      <svg width="12" height="9" viewBox="0 0 12 9" aria-hidden="true"><rect x="0.5" y="0.5" width="11" height="8" fill="none" stroke="#fff"/><path d="M0.5 0.5 L6 5 L11.5 0.5" fill="none" stroke="#fff"/></svg>
      <span>hello@verdantis.com.au</span>
    </div>
    <div class="contact-item contact-web">
      <svg width="12" height="12" viewBox="0 0 12 12" aria-hidden="true"><g fill="none" stroke="#fff" stroke-width="1"><circle cx="6" cy="6" r="5.3"/><ellipse cx="6" cy="6" rx="2.3" ry="5.3"/><path d="M0.7 6 H11.3 M1.5 3.3 H10.5 M1.5 8.7 H10.5"/></g></svg>
      <span>www.verdantis.com.au</span>
    </div>
  </div>
</div>
</body>
</html>
```